PawHush business card

Looking for a fun and cool biz card for a new company with patent pending products. I have products to help and protect dogs hearing. My colors are pantone blue and orange.
Updates

Please add tag line: Protect the ones you love...even your PawHushes!

Target Market(s)

Animal/Dog lovers!

Industry/Entity Type

Retail

Contact Information for Business Card

I'm looking for something simple yet fun with all the info included for biz cards

Colors
0555a3
f78f20

Requirements
Must have
• Logo
Nice to have
• name, website and email
Should not have
• phone number

```html
<!DOCTYPE html>
<html lang="en">
<head>
<meta charset="utf-8">
<title>PawHush Business Card</title>
<link href="https://fonts.googleapis.com/css2?family=Lato:wght@400;700;900&display=swap" rel="stylesheet">
<style>
  :root {
    --brand-blue: #0a3389;
    --brand-orange: #f25a12;
    --ink: #2a2a2a;
    --rule: #8a8a8a;
    --paper: #ffffff;
    --on-blue: #ffffff;
    --backdrop: #ecebe8;
  }
  * { box-sizing: border-box; margin: 0; padding: 0; }
  html, body {
    width: 1200px; height: 900px; overflow: hidden;
    background: var(--backdrop);
    font-family: "Lato", Arial, sans-serif;
  }
  .canvas { position: relative; width: 1200px; height: 900px; }

  .card {
    position: absolute;
    width: 560px; height: 320px;
    box-shadow: 0 10px 28px rgba(0,0,0,0.18);
    overflow: hidden;
  }

  /* Front */
  .card-front {
    left: 70px; top: 140px;
    background: var(--brand-blue);
    display: flex; flex-direction: column; align-items: center; justify-content: center;
    gap: 18px;
  }
  .brand {
    display: flex; align-items: center; gap: 12px;
    font-weight: 900; color: var(--brand-orange);
    letter-spacing: 0.5px; line-height: 1;
  }
  .brand-dot {
    width: 16px; height: 16px; border-radius: 50%;
    background: var(--brand-orange);
  }
  .card-front .brand { font-size: 64px; }
  .tagline {
    font-size: 15px; font-style: italic; color: var(--on-blue);
    letter-spacing: 0.3px;
  }

  /* Back */
  .card-back {
    left: 570px; top: 440px;
    background: var(--paper);
  }
  .card-back .brand {
    position: absolute; right: 34px; top: 36px;
    font-size: 48px;
  }
  .card-back .brand-dot { width: 12px; height: 12px; }
  .rule-top {
    position: absolute; left: 260px; right: 34px; top: 108px;
    height: 1px; background: var(--rule);
  }
  .name-row {
    position: absolute; left: 34px; right: 34px; top: 130px;
    display: flex; align-items: center; gap: 30px;
  }
  .name-row .rule-mid { flex: 1; height: 1px; background: var(--rule); margin-top: 8px; }
  .person-name {
    font-weight: 700; font-size: 21px; color: var(--brand-blue);
    letter-spacing: 0.3px; text-transform: uppercase; white-space: nowrap;
  }
  .person-title {
    position: absolute; left: 34px; top: 158px;
    font-size: 16px; color: var(--ink);
  }
  .address {
    position: absolute; right: 34px; top: 166px;
    text-align: right; font-size: 14px; font-style: normal;
    color: var(--ink); line-height: 1.35;
  }
  .contacts {
    position: absolute; left: 34px; top: 214px;
    list-style: none; font-size: 16px; color: var(--ink);
  }
  .contacts li { display: flex; align-items: center; gap: 8px; line-height: 1.5; }
  .contacts svg { width: 14px; height: 14px; fill: var(--brand-blue); flex: none; }

  .band { position: absolute; bottom: 0; height: 16px; }
  .band-orange { left: 0; width: 66%; background: var(--brand-orange); }
  .band-blue { right: 0; width: 34%; background: var(--brand-blue); }
</style>
</head>
<body>
<main class="canvas">

  <section class="card card-front" aria-label="Card front">
    <div class="brand"><span class="brand-dot"></span><span class="brand-name">PawHush</span></div>
    <p class="tagline">Protect the ones you love...even your PawHushes!</p>
  </section>

  <section class="card card-back" aria-label="Card back">
    <div class="brand"><span class="brand-dot"></span><span class="brand-name">PawHush</span></div>
    <div class="rule-top"></div>

    <div class="name-row">
      <p class="person-name">Daniel Reed</p>
      <div class="rule-mid"></div>
    </div>
    <p class="person-title">Managing Director</p>

    <address class="address">
      421, Address line here<br>Country Name,45452
    </address>

    <ul class="contacts">
      <li>
        <svg viewBox="0 0 16 16" aria-hidden="true"><path d="M1 3h14v10H1z M2 4.2v.4l6 4 6-4v-.4z" fill-rule="evenodd"/></svg>
        info@youremail.com
      </li>
      <li>
        <svg viewBox="0 0 16 16" aria-hidden="true"><circle cx="8" cy="8" r="7"/><path d="M1 8h14M8 1c3 3 3 11 0 14M8 1c-3 3-3 11 0 14" stroke="#fff" stroke-width="1" fill="none"/></svg>
        www.websitename.com
      </li>
    </ul>

    <div class="band band-orange"></div>
    <div class="band band-blue"></div>
  </section>

</main>
</body>
</html>
```